Homemaker goats milk soap label

The name of my farm is Hollow Creek Meadow Farm. I would like to keep my label vintage 1800s is appearance. A linked to my webpage, still under development is http://pelo.trinvemar.com/dev2/fieldkinhome/. This will give you a feel for my theme. Along with other goat and bison by products, I make and sell homemade goat milk soap and I would like a special label to package my fabulous soap.
Updates

Hello Designers, To assist you with designing my label, I have attached a new photo from Lather Haven that shows the type label I am going to use.

Industry/Entity Type

Farm

```html
<!DOCTYPE html>
<html lang="en">
<head>
<meta charset="utf-8">
<title>Goats Milk Soap Label – Hollow Creek Meadow Farm</title>
<link href="https://fonts.googleapis.com/css2?family=Federo&family=Poiret+One&display=swap" rel="stylesheet">
<style>
  :root {
    --brown: #5b3416;
    --paper-yellow: #eef0a8;
    --paper-mint: #d8eecf;
    --paper-cream: #f1e6c2;
    --band: #f8f9ee;
    --page: #ffffff;
  }
  html, body {
    margin: 0;
    width: 1200px;
    height: 1029px;
    overflow: hidden;
    background: var(--page);
  }
  .label {
    position: absolute;
    left: 330px;
    top: 335px;
    width: 540px;
    height: 358px;
    background:
      radial-gradient(circle at 20% 30%, var(--paper-mint) 0, transparent 40%),
      radial-gradient(circle at 75% 25%, var(--paper-cream) 0, transparent 35%),
      radial-gradient(circle at 60% 80%, var(--paper-mint) 0, transparent 40%),
      radial-gradient(circle at 15% 85%, var(--paper-yellow) 0, transparent 40%),
      linear-gradient(120deg, var(--paper-yellow), var(--paper-mint) 55%, var(--paper-yellow));
    overflow: hidden;
  }
  .frame-outer {
    position: absolute;
    left: 8px; top: 8px; right: 8px; bottom: 8px;
    border: 2px solid var(--brown);
  }
  .frame-inner {
    position: absolute;
    left: 14px; top: 14px; right: 14px; bottom: 14px;
    border: 2px solid var(--brown);
  }
  .side-rule {
    position: absolute;
    top: 75px;
    height: 210px;
    width: 2px;
    background: var(--brown);
  }
  .side-rule--left { left: 22px; }
  .side-rule--right { right: 22px; }
  .corner {
    position: absolute;
    width: 44px;
    height: 44px;
    background: var(--brown);
  }
  .corner--tl { left: 30px; top: 27px; clip-path: polygon(0 0, 100% 0, 100% 12%, 12% 12%, 12% 100%, 0 100%); }
  .corner--tr { right: 30px; top: 27px; clip-path: polygon(0 0, 100% 0, 100% 100%, 88% 100%, 88% 12%, 0 12%); }
  .corner--bl { left: 30px; bottom: 27px; clip-path: polygon(0 0, 12% 0, 12% 88%, 100% 88%, 100% 100%, 0 100%); }
  .corner--br { right: 30px; bottom: 27px; clip-path: polygon(88% 0, 100% 0, 100% 100%, 0 100%, 0 88%, 88% 88%); }
  .flourish {
    position: absolute;
    width: 40px;
    height: 16px;
    border-radius: 8px;
    background: var(--brown);
    opacity: 0.85;
  }
  .rule {
    position: absolute;
    height: 2px;
    background: var(--brown);
  }
  .farm-name {
    position: absolute;
    left: 0; right: 0;
    top: 78px;
    text-align: center;
    font-family: "Federo", sans-serif;
    color: var(--brown);
    font-size: 22px;
    line-height: 1.3;
    letter-spacing: 2px;
  }
  .farm-name__mark {
    display: block;
    width: 14px;
    height: 14px;
    margin: 0 auto 8px;
    background: var(--brown);
  }
  .band-line {
    position: absolute;
    left: 8px; right: 8px;
    height: 5px;
    background: var(--brown);
  }
  .band {
    position: absolute;
    left: 14px; right: 14px;
    top: 185px;
    height: 68px;
    background: var(--band);
    border-left: 2px solid var(--brown);
    border-right: 2px solid var(--brown);
    display: flex;
    align-items: center;
    justify-content: center;
  }
  .product-name {
    margin: 0;
    font-family: "Federo", sans-serif;
    font-weight: 400;
    font-size: 42px;
    letter-spacing: 4px;
    color: var(--brown);
  }
  .claims {
    position: absolute;
    left: 0; right: 0;
    top: 276px;
    text-align: center;
    color: var(--brown);
    font-family: "Federo", sans-serif;
  }
  .claims__main { font-size: 25px; letter-spacing: 3px; line-height: 1; }
  .claims__sub { font-size: 13px; letter-spacing: 1px; margin-top: 6px; }
</style>
</head>
<body>
  <div class="label">
    <div class="frame-outer"></div>
    <div class="frame-inner"></div>
    <div class="side-rule side-rule--left"></div>
    <div class="side-rule side-rule--right"></div>

    <div class="corner corner--tl" role="img" aria-label="Ornamental corner bracket"></div>
    <div class="corner corner--tr" role="img" aria-label="Ornamental corner bracket"></div>
    <div class="corner corner--bl" role="img" aria-label="Ornamental corner bracket"></div>
    <div class="corner corner--br" role="img" aria-label="Ornamental corner bracket"></div>

    <div class="flourish" style="left:84px;top:29px" role="img" aria-label="Scroll flourish"></div>
    <div class="rule" style="left:124px;top:37px;width:100px"></div>
    <div class="rule" style="left:322px;top:37px;width:100px"></div>
    <div class="flourish" style="left:420px;top:29px" role="img" aria-label="Scroll flourish"></div>

    <div class="farm-name">
      <span class="farm-name__mark"></span>
      HOLLOW CREEK MEADOW<br>FARM
    </div>

    <div class="band-line" style="top:177px"></div>
    <div class="band">
      <h1 class="product-name">GOATS MILK SOAP</h1>
    </div>
    <div class="band-line" style="top:257px"></div>

    <div class="claims">
      <div class="claims__main">HANDMADE</div>
      <div class="claims__sub">100% NATURAL</div>
    </div>

    <div class="flourish" style="left:104px;top:306px" role="img" aria-label="Scroll flourish"></div>
    <div class="rule" style="left:144px;top:314px;width:56px"></div>
    <div class="rule" style="left:340px;top:314px;width:56px"></div>
    <div class="flourish" style="left:396px;top:306px" role="img" aria-label="Scroll flourish"></div>
  </div>
</body>
</html>
```